Executive Business Consulting for Telco Companies and Telco Start up companies

1.) Looking for an appealing and action oriented business card design.
2.)The target companies to work with start-ups and existing companies that focus on Business to Business applications
3.) For "OKRA", a Belgium based Executive consultancy company specialised in global reach starting from the centre of Europe = Brussels.
4.) Our core competence is the Go To Market in All major global regions, incl North America, Latin America, Asia, Japan, Europe and Africa.
5.) Design should be appealing to CEO, CFO and Venture Funds signalling; Expertise, Stability, Maturity and Commitment
6.) Preferred color scheme is Blue focussed and using a modern FONT.
7.) Logo design is included (uploaded)

Target Market(s)

Telecommunication Market. Companies in a B2B business model, developping services or applications to make business run more profitable

Industry/Entity Type

Business

Contact Information for Business Card

Company Name: OKRA
Name: Joris Vandelay
Titel: Managing Director
Address: Kalkweg 58 , B-9170 Meerdonk , Belgium
Tel: + 32 471 208 364
Email: joris_vandelay@plimbox.example
LinkedIn: be.netprofilo.example/in/jorisvandelay/

Font styles to use
Serif

Colors
0455a3
3277b5

Requirements
Must have
• Second Side Text: Accelerate Market Entry and Growth

```html
<!DOCTYPE html>
<html lang="en">
<head>
<meta charset="utf-8">
<title>OKRA – Business Card</title>
<link href="https://fonts.googleapis.com/css2?family=Cinzel:wght@400;600&family=Lato:wght@400;700;900&display=swap" rel="stylesheet">
<style>
  :root {
    --stage: #1b1c1e;
    --blue-deep: #0455a3;
    --blue-mid: #3277b5;
    --blue-navy: #1f3f73;
    --slate: #55585c;
    --paper: #ffffff;
    --paper-shade: #e6e8eb;
    --ink: #2b2b2b;
  }
  * { box-sizing: border-box; margin: 0; padding: 0; }
  html, body { width: 1200px; height: 871px; overflow: hidden; background: var(--stage); }
  .stage {
    width: 1200px; height: 871px;
    display: flex; flex-direction: column; align-items: center; justify-content: center; gap: 28px;
  }
  .card {
    width: 700px; height: 400px; position: relative; overflow: hidden;
    border-radius: 4px; box-shadow: 0 14px 40px rgba(0,0,0,.55);
  }

  /* Back side */
  .card--back {
    background: linear-gradient(160deg, var(--paper) 0%, var(--paper-shade) 100%);
    display: flex; flex-direction: column; align-items: center; justify-content: center; gap: 34px;
  }
  .brand { display: flex; align-items: center; gap: 22px; }
  .brand__dot { width: 96px; height: 96px; border-radius: 50%; background: var(--blue-mid); flex: none; }
  .brand__name {
    font-family: "Lato", sans-serif; font-weight: 900; font-size: 104px;
    letter-spacing: 4px; color: var(--blue-navy); line-height: 1; white-space: nowrap;
  }
  .tagline {
    font-family: "Cinzel", serif; font-size: 19px; letter-spacing: 3px; color: var(--blue-navy);
  }

  /* Front side */
  .card--front { background: var(--paper); }
  .front__head { position: absolute; left: 44px; top: 42px; }
  .person {
    font-family: "Cinzel", serif; font-weight: 400; font-size: 36px; color: var(--ink); letter-spacing: 1px; line-height: 1;
  }
  .role {
    font-family: "Lato", sans-serif; font-weight: 700; font-size: 14px; color: var(--blue-deep);
    letter-spacing: 5px; text-transform: uppercase; margin-top: 4px; padding-left: 2px;
  }
  .front__band {
    position: absolute; left: 0; right: 0; top: 150px; bottom: 0;
    background: linear-gradient(180deg, var(--blue-mid) 0%, var(--blue-deep) 100%);
  }
  .tab--shade {
    position: absolute; left: 372px; top: 115px; width: 120px; height: 200px;
    background: var(--slate); border-radius: 22px;
  }
  .tab--brand {
    position: absolute; left: 420px; right: 0; top: 110px; height: 210px;
    background: linear-gradient(160deg, var(--blue-mid), var(--blue-deep));
    border-radius: 26px 0 0 26px; box-shadow: -4px 6px 14px rgba(0,0,0,.35);
    display: flex; align-items: center; justify-content: center; gap: 12px;
  }
  .tab--brand .brand__dot { width: 40px; height: 40px; background: rgba(255,255,255,.85); }
  .tab--brand .brand__name { font-size: 52px; color: var(--paper); letter-spacing: 2px; }
  .contact {
    position: absolute; left: 44px; top: 178px; list-style: none;
    font-family: "Lato", sans-serif; font-size: 15px; color: var(--paper); line-height: 1.55;
  }
  .contact li { display: flex; align-items: center; gap: 10px; }
  .contact svg { width: 13px; height: 13px; flex: none; fill: var(--paper); }
  .profile {
    position: absolute; left: 140px; top: 340px; display: flex; align-items: center; gap: 10px;
    font-family: "Lato", sans-serif; font-size: 14px; letter-spacing: 2.5px; text-transform: uppercase; color: var(--paper);
  }
  .profile__square { width: 16px; height: 16px; background: var(--paper); border-radius: 2px; }
</style>
</head>
<body>
<main class="stage">
  <section class="card card--back" aria-label="Card back">
    <div class="brand">
      <span class="brand__dot"></span>
      <span class="brand__name">OKRA</span>
    </div>
    <p class="tagline">Accelerate Market Entry and Growth</p>
  </section>

  <section class="card card--front" aria-label="Card front">
    <div class="front__head">
      <h1 class="person">Joris Vandelay</h1>
      <p class="role">Managing Director</p>
    </div>
    <div class="front__band"></div>
    <div class="tab--shade"></div>
    <div class="tab--brand">
      <span class="brand__dot"></span>
      <span class="brand__name">OKRA</span>
    </div>
    <ul class="contact">
      <li>
        <svg viewBox="0 0 12 16"><path d="M6 0a6 6 0 0 0-6 6c0 4.5 6 10 6 10s6-5.5 6-10a6 6 0 0 0-6-6zm0 8.5A2.5 2.5 0 1 1 6 3.5a2.5 2.5 0 0 1 0 5z"/></svg>
        Kalkweg 58, B-9170 Meerdonk Belgium
      </li>
      <li>
        <svg viewBox="0 0 16 16"><path d="M1 5c0-2 3-3 7-3s7 1 7 3v1h-4V5H5v1H1zM3 7h10l2 7H1z"/></svg>
        + 32 471 208 364
      </li>
      <li>
        <svg viewBox="0 0 16 12"><path d="M0 0h16v1.5L8 7 0 1.5zM0 3.5l8 5.5 8-5.5V12H0z"/></svg>
        joris_vandelay@plimbox.example
      </li>
    </ul>
    <div class="profile">
      <span class="profile__square"></span>
      be.netprofilo.example/in/jorisvandelay/
    </div>
  </section>
</main>
</body>
</html>
```